Oven Cleaning Business owner needs business card design

Hi there,
Would like for a business card to be designed for myself, the owner of a professional oven cleaning business on the Sunshine Coast.
Would like it to look sleek, and modern-ish. Bit creative is encouraged too.
Include following:
Name/title: Corin de Walbrek, Owner
Phone number: 1300 482 906
Email: info@kitchenlustrely.com.au
Website: www.kitchenlustrely.com.au

```html
<!DOCTYPE html>
<html lang="en">
<head>
<meta charset="UTF-8">
<title>Kitchen Lustrely — Business Card</title>
<link href="https://fonts.googleapis.com/css2?family=Montserrat:wght@400;500;700;800&display=swap" rel="stylesheet">
<style>
  :root {
    --teal: #52c4cb;
    --teal-dark: #3fb1b8;
    --ink: #111417;
    --paper: #ffffff;
    --backdrop: #2b2d30;
  }
  html, body {
    margin: 0;
    padding: 0;
    width: 1200px;
    height: 960px;
    overflow: hidden;
    background: var(--backdrop);
    font-family: "Montserrat", Arial, sans-serif;
  }
  .canvas {
    position: relative;
    width: 1200px;
    height: 960px;
  }
  .card {
    position: absolute;
    width: 700px;
    height: 400px;
    border-radius: 22px;
    overflow: hidden;
    box-shadow: 0 18px 40px rgba(0,0,0,0.45);
  }
  /* Front */
  .card-front {
    left: 80px;
    top: 40px;
    background: var(--teal);
    display: flex;
    align-items: center;
    justify-content: center;
  }
  .brand {
    display: flex;
    align-items: center;
    gap: 16px;
    font-weight: 800;
    letter-spacing: 0.06em;
    text-transform: uppercase;
  }
  .brand-dot {
    width: 28px;
    height: 28px;
    border-radius: 50%;
  }
  .card-front .brand { color: var(--paper); font-size: 46px; }
  .card-front .brand-dot { background: var(--paper); }

  /* Back */
  .card-back {
    left: 420px;
    top: 500px;
    background: var(--paper);
  }
  .card-back .brand {
    position: absolute;
    left: 40px;
    top: 150px;
    width: 260px;
    flex-direction: column;
    gap: 12px;
    color: var(--teal);
    font-size: 30px;
    text-align: center;
    line-height: 1.1;
  }
  .card-back .brand-dot { background: var(--teal); width: 36px; height: 36px; }
  .divider {
    position: absolute;
    left: 320px;
    top: 95px;
    width: 2px;
    height: 160px;
    background: var(--teal);
  }
  .details {
    position: absolute;
    left: 345px;
    top: 70px;
    color: var(--ink);
  }
  .person-name {
    margin: 0;
    color: var(--teal);
    font-size: 25px;
    font-weight: 800;
    text-transform: uppercase;
    letter-spacing: -0.01em;
  }
  .person-title {
    margin: 4px 0 22px 8px;
    font-size: 17px;
    font-weight: 500;
  }
  .contact-list {
    list-style: none;
    margin: 0;
    padding: 0 0 0 8px;
  }
  .contact-list li {
    display: flex;
    align-items: center;
    gap: 12px;
    font-size: 16px;
    font-weight: 500;
    margin-bottom: 9px;
  }
  .contact-icon {
    width: 18px;
    height: 18px;
    flex: none;
  }
  .footer-band {
    position: absolute;
    left: 0;
    bottom: 0;
    width: 700px;
    height: 400px;
    pointer-events: none;
  }
</style>
</head>
<body>
<main class="canvas">

  <section class="card card-front" aria-label="Card front">
    <div class="brand">
      <span class="brand-dot"></span>
      <span>Kitchen Lustrely</span>
    </div>
  </section>

  <section class="card card-back" aria-label="Card back">
    <svg class="footer-band" viewBox="0 0 700 400" aria-hidden="true">
      <polygon fill="var(--ink)" points="0,360 240,360 236,368 0,368"/>
      <polygon fill="var(--teal)" points="0,372 236,372 250,340 300,340 300,348 256,348 244,376 0,376"/>
      <polygon fill="var(--ink)" points="312,340 500,340 508,326 500,326 312,326"/>
      <polygon fill="var(--teal)" points="0,384 250,384 262,352 505,352 520,310 700,310 700,400 0,400"/>
    </svg>

    <div class="brand">
      <span class="brand-dot"></span>
      <span>Kitchen<br>Lustrely</span>
    </div>

    <div class="divider"></div>

    <div class="details">
      <h1 class="person-name">Corin de Walbrek</h1>
      <p class="person-title">Owner</p>
      <ul class="contact-list">
        <li>
          <svg class="contact-icon" viewBox="0 0 24 24"><path fill="var(--teal)" d="M6.6 10.8a15 15 0 0 0 6.6 6.6l2.2-2.2a1 1 0 0 1 1-.25 11.4 11.4 0 0 0 3.6.57 1 1 0 0 1 1 1V20a1 1 0 0 1-1 1A17 17 0 0 1 3 4a1 1 0 0 1 1-1h3.5a1 1 0 0 1 1 1c0 1.25.2 2.45.57 3.57a1 1 0 0 1-.25 1z"/></svg>
          1300 482 906
        </li>
        <li>
          <svg class="contact-icon" viewBox="0 0 24 24"><path fill="var(--teal)" d="M2 5h20v14H2z"/><path fill="none" stroke="#fff" stroke-width="1.8" d="M2.5 5.5 12 13l9.5-7.5"/></svg>
          info@kitchenlustrely.com.au
        </li>
        <li>
          <svg class="contact-icon" viewBox="0 0 24 24"><circle cx="12" cy="12" r="10" fill="var(--teal)"/><path fill="none" stroke="#fff" stroke-width="1.4" d="M2 12h20M12 2c3 3 3 17 0 20M12 2c-3 3-3 17 0 20"/></svg>
          www.kitchenlustrely.com.au
        </li>
      </ul>
    </div>
  </section>

</main>
</body>
</html>
```